I need a business card for myself, being a proprietor of a funeral parlor based in Manila. I'd like the card to have either of the following:
White Font on Black Background
or
Black Font on White Background
No logo is needed however I will appreciate any efforts to show a symbol of eternal happiness, aptly designed with above mentioned colors in mind.
Company name, address and contact on the lower right corner.
Logo or symbol anywhere.
Quillstone Funeral Services
+639174826351
darvik4521@pelmora.com
corner of Brisco Avenue and Velhurst Street
Makati City, Philippines
Thank you.
Update: Please include a small dove in your design. You are free to choose where you would like it on the card.

```html
<!DOCTYPE html>
<html lang="en">
<head>
<meta charset="utf-8">
<title>Quillstone Funeral Services – Business Card</title>
<link rel="stylesheet" href="https://fonts.googleapis.com/css2?family=Open+Sans:wght@400;600&display=swap">
<style>
  :root {
    --page-bg: #c9c9c9;
    --card-black: #0c0c0c;
    --card-charcoal: #262626;
    --ink-white: #f2f2f2;
    --ink-soft: #d6d6d6;
  }
  html, body {
    margin: 0;
    width: 1200px;
    height: 880px;
    overflow: hidden;
    background: var(--page-bg);
    font-family: "Open Sans", Arial, sans-serif;
  }
  .card {
    position: absolute;
    left: 100px;
    top: 160px;
    width: 1000px;
    height: 560px;
    color: var(--ink-white);
    box-sizing: border-box;
  }
  .card-texture {
    position: absolute;
    inset: 0;
    background:
      linear-gradient(120deg, var(--card-black) 0%, var(--card-charcoal) 45%, #1a1a1a 60%, var(--card-black) 100%);
  }
  .brand {
    position: absolute;
    left: 60px;
    top: 95px;
    display: flex;
    align-items: center;
    gap: 30px;
  }
  .brand-mark {
    width: 64px;
    height: 64px;
    border-radius: 50%;
    background: var(--ink-white);
    flex: none;
  }
  .brand-name {
    margin: 0;
    font-weight: 400;
    font-size: 62px;
    line-height: 1.05;
    font-variant: small-caps;
    letter-spacing: 1px;
    color: var(--ink-white);
  }
  .contact-values {
    position: absolute;
    right: 60px;
    top: 255px;
    margin: 0;
    text-align: right;
    font-size: 21px;
    line-height: 1.3;
    color: var(--ink-soft);
  }
  .contact-labels {
    position: absolute;
    left: 60px;
    top: 390px;
    width: 160px;
    margin: 0;
    text-align: right;
    font-weight: 600;
    font-size: 24px;
    line-height: 1.25;
    color: var(--ink-white);
  }
</style>
</head>
<body>
  <section class="card" aria-label="Business card">
    <div class="card-texture" role="img" aria-label="Dark brushed charcoal card surface with a faint diamond pattern"></div>
    <div class="brand">
      <span class="brand-mark" aria-hidden="true"></span>
      <h1 class="brand-name">Quillstone Funeral<br>Services</h1>
    </div>
    <p class="contact-values">
      +639174826351<br>
      darvik4521@pelmora.com<br>
      Corner of Brisco Avenue and Velhurst Street<br>
      Makati City, Philippines
    </p>
    <p class="contact-labels">
      Phone:<br>
      Email:<br>
      Address:
    </p>
  </section>
</body>
</html>
```